SUPPLEMENT BOTTLE LABEL: DRUMMOND

We need a NEW FRESH look to her labels. Something contemporary, clean and professional. The colors need to remain the same but everything else can change, even the logo.

THE CURRENT LABEL IS ATTACHED IN PDF FORMAT

Target Market(s)

WOMEN BETWEEN 35-60

Requirements
Must have
• SAME COLORS
• FRESH
• CLEAN

```html
<!DOCTYPE html>
<html lang="en">
<head>
<meta charset="UTF-8">
<title>Vital Renew – Cleanse Chocolate Label</title>
<link href="https://fonts.googleapis.com/css2?family=Itim&family=Bungee&display=swap" rel="stylesheet">
<style>
  :root {
    --bg: #ece8f2;
    --label-light: #8fcf3a;
    --label-mid: #72b52a;
    --label-dark: #5a9a1f;
    --ink: #13301a;
    --ink-soft: #1d3d22;
    --paper: #ffffff;
  }
  * { margin: 0; padding: 0; box-sizing: border-box; }
  html, body {
    width: 1200px; height: 1200px; overflow: hidden;
    background: var(--bg);
  }
  .canvas {
    width: 1200px; height: 1200px;
    display: flex; align-items: center; justify-content: center;
  }
  .label {
    position: relative;
    width: 900px; height: 1080px;
    background: radial-gradient(ellipse at 50% 38%, var(--label-light) 0%, var(--label-mid) 55%, var(--label-dark) 100%);
    color: var(--ink);
    font-family: "Itim", cursive;
    display: flex; flex-direction: column; align-items: center;
    padding-top: 150px;
    text-align: center;
  }
  .label-texture {
    position: absolute; inset: 0;
    background: radial-gradient(circle at 50% 45%, rgba(255,255,255,0.12), rgba(255,255,255,0) 60%);
    pointer-events: none;
  }
  .brand-name {
    position: relative;
    font-size: 118px;
    line-height: 1;
    color: var(--ink);
    letter-spacing: 1px;
  }
  .flavor-box {
    position: relative;
    margin-top: 56px;
    border: 3px solid var(--ink);
    border-radius: 22px;
    padding: 12px 26px 6px;
  }
  .flavor-title {
    font-family: "Bungee", sans-serif;
    font-size: 92px;
    line-height: 1.08;
    color: var(--ink);
    letter-spacing: 2px;
  }
  .flavor-tag {
    position: relative;
    margin-top: -18px;
    background: var(--ink);
    color: var(--paper);
    font-size: 42px;
    padding: 2px 30px 6px;
    border-radius: 30px;
  }
  .product-info {
    position: relative;
    margin-top: 52px;
    font-size: 36px;
    line-height: 1.4;
    color: var(--ink-soft);
  }
  .net-weight {
    position: relative;
    margin-top: 70px;
    display: flex; align-items: center; gap: 14px;
    font-size: 32px;
    color: var(--ink-soft);
  }
  .net-weight .rule {
    width: 70px; height: 2px; background: var(--ink-soft);
  }
</style>
</head>
<body>
  <main class="canvas">
    <section class="label">
      <div class="label-texture"></div>
      <h1 class="brand-name">Vital Renew</h1>
      <div class="flavor-box">
        <h2 class="flavor-title">CLEANSE<br>CHOCOLATE</h2>
      </div>
      <p class="flavor-tag">with other natural flavors</p>
      <div class="product-info">
        <p>Collagen, Multivitamin, Mineral &amp;</p>
        <p>Herbal Dietary Supplement Powder</p>
        <p>Notice: Use this product as a food supplement only.</p>
        <p>Do not use for weight reduction.</p>
      </div>
      <div class="net-weight">
        <span class="rule"></span>
        <span>NET WT. 1.21 LBS (551.2 G)</span>
        <span class="rule"></span>
      </div>
    </section>
  </main>
</body>
</html>
```